A new presentation to our clients

we are a Real Estate agency, our website is www.lirotama.com and it’s time to have a new, fashion and remarcable Business Card. we want to differentiate ourselves from other companies so we want a business card that differentiates us. we want the business card to impact our customers. in the competitive market that we have today, we have to be different and it is this difference that we seek

Target Market(s)

Real Estate Clients

Contact Information for Business Card

We search a totaly diferent card from the usual

Font styles to use
Sans Serif

Colors
e34197

Requirements
Must have
• Logo, adress, phone contact, e-mail, photo, and our website
Nice to have
• We would like to see a modern business card
Should not have
• Houses or building draws

```html
<!DOCTYPE html>
<html lang="en">
<head>
<meta charset="utf-8">
<title>Lirotama Business Card</title>
<link rel="stylesheet" href="https://fonts.googleapis.com/css2?family=Arimo:wght@400;700&display=swap">
<style>
  :root {
    --brand-pink: #e71f6b;
    --ink-grey: #555555;
    --muted-grey: #8a8a8a;
    --card-white: #ffffff;
    --backdrop: #ece9e4;
  }
  * { margin: 0; padding: 0; box-sizing: border-box; }
  html, body {
    width: 1125px;
    height: 1200px;
    overflow: hidden;
    background: var(--backdrop);
    font-family: "Arimo", Arial, sans-serif;
  }
  .business-card {
    position: absolute;
    left: 150px;
    top: 361px;
    width: 826px;
    height: 471px;
    background: var(--card-white);
    box-shadow: 0 2px 6px rgba(0,0,0,0.25);
  }
  .brand-name {
    position: absolute;
    left: 68px;
    top: 186px;
    font-size: 62px;
    font-weight: 700;
    color: var(--brand-pink);
    letter-spacing: 1px;
    line-height: 1;
  }
  .contact-block {
    position: absolute;
    left: 488px;
    top: 106px;
    color: var(--ink-grey);
  }
  .person-name {
    font-size: 29px;
    font-weight: 700;
    color: var(--brand-pink);
    line-height: 32px;
  }
  .person-title {
    font-size: 19px;
    color: var(--muted-grey);
    line-height: 22px;
    margin-bottom: 14px;
  }
  .address-line,
  .contact-line {
    font-size: 19px;
    line-height: 25px;
  }
  .address { margin-bottom: 11px; }
  .contact-list { padding-left: 5px; line-height: 26px; }
  .contact-line { line-height: 26px; }
  .web-band {
    position: absolute;
    left: 0;
    top: 415px;
    width: 100%;
    height: 35px;
    background: var(--brand-pink);
    color: var(--card-white);
    font-size: 18px;
    letter-spacing: 10px;
    text-align: center;
    line-height: 35px;
    padding-left: 10px;
  }
</style>
</head>
<body>
  <div class="business-card">
    <div class="brand-name">Lirotama</div>

    <div class="contact-block">
      <div class="person-name">MARTA RIBEIRO</div>
      <div class="person-title">CEO/FOUNDER</div>
      <div class="address">
        <div class="address-line">Rua das Laranjeiras, 148</div>
        <div class="address-line">4410-052, Porto Sul</div>
      </div>
      <div class="contact-list">
        <div class="contact-line">P: (+351) 210 486 352</div>
        <div class="contact-line">F: (+351) 210 486 359</div>
        <div class="contact-line">E: geral@lirotama.com</div>
      </div>
    </div>

    <div class="web-band">www.lirotama.com</div>
  </div>
</body>
</html>
```